Q-LINK Technical One-Sheet

Requesting page design for a technical sales "slick sheet". This design should be full page with the following points below:
- Incorporate the pictures, logo provided
- Use color scheme of black, white, green and font (see attached read me file and art). multiple logos are provided: use any, all...whatever.
- Space for technical specifications, overview and marketing bullets

Technology Overview
- quality of service server for telecommunications industry
- used within a network's infrastructure: cell tower, network switch, etc.
- pix of server is attached: "Q-LINK"

I have provided a sample "one-sheet" from a previous project to use as an example: but NOT the model.

I would prefer this page design to be edited by my firm for later projects/tehcnologies. User friendly formats are preferred for description edits and follow up efforts.

```html
<!DOCTYPE html>
<html lang="en">
<head>
<meta charset="utf-8">
<title>Halvard Systems – Technical One-Sheet</title>
<link rel="stylesheet" href="https://fonts.googleapis.com/css2?family=Questrial&family=Tinos&display=swap">
<style>
  :root {
    --header-green: #5a9b43;
    --lime: #8dc63f;
    --headline-gray: #a3a3a3;
    --text: #1e1e1e;
    --footer-gray: #cdcdcd;
    --logo-dark: #262626;
    --white: #ffffff;
  }
  * { margin: 0; padding: 0; box-sizing: border-box; }
  html, body { width: 927px; height: 1200px; overflow: hidden; background: var(--white); }
  .sheet { position: relative; width: 927px; height: 1200px; overflow: hidden; font-family: "Tinos", "Times New Roman", serif; color: var(--text); }

  .masthead { position: absolute; left: 0; top: 0; width: 927px; height: 179px; background: var(--header-green); display: flex; align-items: center; justify-content: center; gap: 20px; }
  .brand-mark { width: 74px; height: 74px; border-radius: 50%; background: var(--lime); }
  .brand-name { font-family: "Questrial", "Century Gothic", sans-serif; font-size: 52px; letter-spacing: 6px; color: var(--logo-dark); }

  .product-photo { position: absolute; left: 27px; top: 210px; width: 292px; height: 118px; }

  .headline { position: absolute; left: 357px; top: 226px; width: 540px; font-family: "Questrial", "Century Gothic", sans-serif; font-size: 36px; line-height: 45px; color: var(--headline-gray); font-weight: 700; }
  .headline .accent { color: var(--lime); font-weight: 400; }

  .specs { position: absolute; left: 0; top: 424px; width: 329px; height: 679px; background: var(--lime); color: var(--white); padding: 14px 22px 0 22px; }
  .specs h2 { font-family: "Questrial", "Century Gothic", sans-serif; font-size: 23px; font-weight: 400; margin-bottom: 10px; }
  .specs p { font-size: 15px; line-height: 19.5px; margin-bottom: 19px; }
  .specs p.tight { margin-bottom: 0; }

  .column { position: absolute; top: 448px; font-size: 15px; line-height: 20px; }
  .column-left { left: 350px; width: 242px; }
  .column-right { left: 636px; width: 272px; top: 434px; }
  .column h3 { font-family: "Questrial", "Century Gothic", sans-serif; color: var(--lime); font-size: 18px; font-weight: 700; line-height: 22px; margin-bottom: 2px; }
  .column h3.marketing { margin-top: 26px; }
  .column-right p { margin-bottom: 20px; }

  .divider { position: absolute; left: 606px; top: 439px; width: 1px; height: 652px; background: var(--lime); }

  .footer { position: absolute; left: 0; bottom: 0; width: 927px; height: 53px; background: var(--footer-gray); display: flex; align-items: center; justify-content: center; font-size: 16px; color: var(--text); }
</style>
</head>
<body>
<div class="sheet">
  <header class="masthead">
    <span class="brand-mark"></span>
    <span class="brand-name">HALVARD SYSTEMS</span>
  </header>

  <svg class="product-photo" role="img" aria-label="Photo of the Q-LINK 2U rack server with front drive bays" viewBox="0 0 292 118">
    <defs>
      <linearGradient id="serverTone" x1="0" y1="0" x2="0" y2="1">
        <stop offset="0" stop-color="#b9bcbf"/>
        <stop offset="1" stop-color="#5d6166"/>
      </linearGradient>
    </defs>
    <rect width="292" height="118" fill="url(#serverTone)"/>
  </svg>

  <h1 class="headline">Quick Overview of this awesome <span class="accent">product then continue with marketing b.</span></h1>

  <aside class="specs">
    <h2>Technical Specifications</h2>
    <p>Restis simentur aute non por audae lab iumquae pos dolora venim voluptae modissimus, que prat voluptiis rem qui ut hitium quam sinciendiae nimperspic tenienienis se aut dolupid elignietur, nimincit facerio nsedit arum, simincim quas adigent esciassi is ad mi, sintotae. Lendam, occuptur, sequamus es am recto volum quundam, quodi velicat ionsedit qui voluptate nectatu ribeaquid eum voluptas doluptae estia poresto molenis eatquam inci dolorib usanderum id mil inullac idebis maiostia aut enisquaes atem demquis arum quam quunt plaborem nihit veri reperferate volum</p>
    <p class="tight">Bis et aut fuga. Oremolu pistiores enimolum velicte moluptatur maionsent aut alit quat ut ra conem que nonseque liquiae nos restia coreiur aut dolecea-turia que duciis nusa voloribus.</p>
    <p>Os sinctore solut aborecus, officiis ventisc itaquae rumquiae. Nem apicatur, volupta erume la venis quis sunt quod magnimet lam faccabo reicte num fugiatiorum ent, verum receatus maximai onsector sundellestin pratus</p>
  </aside>

  <section class="column column-left">
    <h3>Overview</h3>
    <p>•Restis simentur aute non por audae lab iumquae pos dolora venim voluptae modissimus, que prat voluptiis rem qui ut hitium quam sinciendiae nimperspic tenienienis se aut dolupid elignietur</p>
    <p>•Restis simentur aute non por audae lab iumquae pos dolora venim voluptae modissimus, que prat voluptiis rem qui ut hitium quam sinciendiae nimperspic tenienienis se aut dolupid elignietur</p>
    <p>•Restis simentur aute non por audae lab iumquae pos dolora venim voluptae modissimus, que prat voluptiis rem qui ut hitium quam sinciendiae nimperspic tenienienis se aut dolupid elignietur</p>
    <h3 class="marketing">Marketing Bullets s</h3>
    <p>•Restis simentur aute non por audae lab iumquae pos dolora venim voluptae modissimus, que prat voluptiis rem qui ut hitium quam sinciendiae nimperspic tenienienis se aut dolupid else aut dolupid elignietur</p>
  </section>

  <div class="divider"></div>

  <section class="column column-right">
    <p>•Restis simentur aute non por audae lab iumquae pos dolora venim voluptae modissimus, que prat voluptiis rem qui ut hitium quam sinciendiae nimperspic tenienienis se aut dolupid elignietur</p>
    <p>•Restis simentur aute non por audae lab iumquae pos dolora venim voluptae modissimus, que prat voluptiis rem qui ut hitium quam sinciendiae nimperspic tenienienis se aut dolupid elignietur</p>
    <p>•Restis simentur aute non por audae lab iumquae pos dolora venim voluptae modissimus, que prat voluptiis rem qui ut hitium quam sinciendiae nimperspic tenienienis se aut dolupid elignietur</p>
    <p>•Restis simentur aute non por audae lab iumquae pos dolora venim voluptae modissimus, que prat voluptiis rem qui ut hitium quam sinciendiae nimperspic tenienienis se aut dolupid else aut dolupid elignietur</p>
  </section>

  <footer class="footer">Address • City, State Zip Code • (555) 014 -2290 • email@yourcompanysite.com • www.yourcompanysite.com</footer>
</div>
</body>
</html>
```